Product Packaging for an Aquarium Company
Brivan Aquatics
Product Packaging for an Aquarium Company - Animals
Creative Brief
Our company, Brivan Aquatics is looking for a design for custom packaging to support our main line of aquariums. We are different from other companies as we have a product that is stylish, refined, and elegant. They feature smooth lines and sharp color contrasts.
Animals
We are in the business of wholesale and distribution with the end point being retailers in the aquatic or pet hobby.
The custom packaging design will have to have our logo and company name, Brivan Aquatics visible on the front of the packaging. I want the packaging to reflect the style of our aquariums. I will upload some photos for inspiration. I want to have a white bottle or packaging, or a subtle grey/silver with a sharp contrast of another color. I would be interested to see the addition of a wave or large bubble that would contain the picture of the contents of the packaging.

```html
<!DOCTYPE html>
<html lang="en">
<head>
<meta charset="utf-8">
<title>Brivan Aquatics – Bottle Labels</title>
<link rel="stylesheet" href="https://fonts.googleapis.com/css2?family=Lora:wght@400&family=Open+Sans:wght@400&display=swap">
<style>
  :root {
    --stage: #000000;
    --label: #ffffff;
    --ink: #1a1a1a;
    --wave-blue: #1f3f9e;
    --wave-black: #0b0b0b;
    --wave-grey: #9a9a9a;
    --caption: #ffffff;
  }
  * { margin: 0; padding: 0; box-sizing: border-box; }
  html, body { width: 1200px; height: 562px; overflow: hidden; background: var(--stage); }
  .canvas { position: relative; width: 1200px; height: 562px; background: var(--stage); }
  .label {
    position: absolute; top: 92px; width: 216px; height: 365px;
    background: var(--label); overflow: hidden;
  }
  .label--back { left: 350px; }
  .label--front { left: 634px; }
  .label__wave-area {
    position: absolute; left: 0; right: 0; bottom: 0;
    background: linear-gradient(180deg, var(--label) 0%, var(--wave-blue) 22%, var(--wave-black) 55%, var(--wave-grey) 100%);
  }
  .label--back .label__wave-area { height: 110px; }
  .label--front .label__wave-area { height: 165px; }
  .brand {
    position: absolute; left: 0; right: 0;
    display: flex; align-items: center; justify-content: center; gap: 5px;
    font-family: "Lora", Georgia, serif; font-weight: 400; color: var(--ink);
  }
  .brand__dot { width: 9px; height: 9px; border-radius: 50%; background: var(--ink); }
  .label--back .brand { top: 22px; font-size: 12px; }
  .label--front .brand { top: 126px; font-size: 13px; }
  .label--front .brand__dot { width: 11px; height: 11px; }
  .directions {
    position: absolute; left: 20px; right: 18px; top: 52px;
    font-family: "Open Sans", Arial, sans-serif; font-size: 5.6px; line-height: 1.45;
    color: var(--ink); text-align: justify;
  }
  .directions p { margin-bottom: 6px; }
  .directions .directions__note { margin-top: 10px; }
  .caption {
    position: absolute; left: 0; right: 0; top: 478px; text-align: center;
    font-family: "Open Sans", Arial, sans-serif; font-size: 15px; line-height: 1.3;
    color: var(--caption);
  }
</style>
</head>
<body>
<main class="canvas">

  <section class="label label--back" aria-label="Back label">
    <div class="label__wave-area" role="img" aria-label="Decorative blue, black and grey wave band"></div>
    <div class="brand"><span class="brand__dot"></span><span class="brand__name">Brivan Aquatics</span></div>
    <div class="directions">
      <p>Our water conditioner keeps your aquarium clear and balanced. Add the dose shown below when you set up a new tank and each time you change part of the water.</p>
      <p>Shake well before use. Add five millilitres for every twenty litres of aquarium water. Safe for all freshwater fish, plants and filter bacteria when used as directed.</p>
      <p>Store in a cool dry place away from direct sunlight. Keep out of reach of children. Do not drink. Close the cap tightly after each use.</p>
      <p class="directions__note">Made for Brivan Aquatics. Net contents one litre.</p>
    </div>
  </section>

  <section class="label label--front" aria-label="Front label">
    <div class="label__wave-area" role="img" aria-label="Decorative blue, black and grey wave band"></div>
    <div class="brand"><span class="brand__dot"></span><span class="brand__name">Brivan Aquatics</span></div>
  </section>

  <p class="caption">Label bottle 13 X 16 CM<br>1 L</p>

</main>
</body>
</html>
```